International game business needs app design

We are planning to release a new mobile game on Qbe5 which requires a fresh, flat, reduced and functional design, fulfilling Brindle’s Qbe5 design guidelines
.
The design shall be created for a dashboard, where players should be able to pick levels (icon + short description; 300+ levels), opponents (icon/photo/avatar image + short description; 5-100) and read/delete system/chat messages (icon, 2-3 actions (delete, accept/decline), text with up to 500 characters; 1-100 entries), Menu bar (settings, shop, leaderboards, achievements, and one or two more menu items) It must consider means to search/select levels and opponents. Would be nice to have an option to start playing immediately (with a random opponent on a random level)

Overall Style/Look: fresh, flat, functional, lot’s of free space, warm color scheme. If full screen images are being used it must be considered that there are user-generated photos or avatars which have to work with it in combination

Ideally the design is responsive and would work both on a smartphone and a tablet. Smartphone is top priority, tablet is optional.

The app will be a game for women predominantly, aged 25-35, with higher education and household net income, which should be reflected in color scheme, icons and navigation.

Some of us like flat design, so you might stick to that or impress all of us with something completely new!

The winner will have the chance to design all screens for the app and will have access to a much bigger budget.

UPDATE: A wireframe is attached - but you don't have to follow the depicted layout. Actually it would be highly appreciated if you could come up with something new. The only important thing is that all the listed components must appear somehow on the dashboard.

Target Market(s)

US, AU, NZ, GB, CA

Industry/Entity Type

Education

Colors

Designer to choose colors to be used in the design.

Requirements
Must have
• All the functional components described above.
Design must be in line with Qbe5 design guidelines https://makers.brindlehub.example/library/qbe/documentation/UserExperience/Conceptual/TouchGuide/index.html
Nice to have
• We would like to have someone with the following attributes:
* minimum 5 qbe design in your past at least 2 of them responsive – please provide links to the apps you created
* besides UI designer skills would be nice you to have UX skills

The most important factors for us are quality, creativity, speed, flexibility (“be able to take criticism into account”)
Should not have
• We don’t want a girly design so please don’t use too much pinks, flowers and such. The design should be acceptable by men too.

```html
<!DOCTYPE html>
<html lang="en">
<head>
<meta charset="utf-8">
<title>Lets Play Game – Dashboard</title>
<link rel="stylesheet" href="https://fonts.googleapis.com/css2?family=Roboto:wght@300;400;500;700&family=Roboto+Condensed:wght@400;700&display=swap">
<style>
:root{
  --bg-top:#f7931e;
  --bg-bottom:#f05a28;
  --cream:#fde4bf;
  --brown-dark:#5a2708;
  --brown:#8a3b0c;
  --card:#c9650f;
  --card-edge:#9c4608;
  --accent:#e8501c;
  --circle:#e84a0a;
  --gold:#ffd54a;
  --bubble:#fdb04a;
  --bubble-fold:#c9501c;
  --pill:#f39a2c;
  --msg-text:#b8460e;
  --white:#ffffff;
  --hex-line:#7fd3e8;
  --profile-line:#f2a03a;
}
*{box-sizing:border-box;margin:0;padding:0}
html,body{width:677px;height:1200px;overflow:hidden}
body{background:var(--bg-bottom);font-family:"Roboto",sans-serif}
.screen{position:absolute;left:0;top:0;width:640px;height:1136px;transform:scale(1.0578,1.0563);transform-origin:0 0;
  background:linear-gradient(160deg,var(--bg-top) 0%,#f4782a 55%,var(--bg-bottom) 100%);overflow:hidden}
.abs{position:absolute}

/* status bar */
.status{top:0;left:0;width:640px;height:36px;color:var(--white);font-size:22px;font-weight:300}
.status .dots{left:14px;top:10px;display:flex;gap:3px}
.status .dots span{width:12px;height:12px;border-radius:50%;background:var(--white)}
.status .dots span.off{background:none;border:1.5px solid var(--white)}
.status .carrier{left:93px;top:4px}
.status .pct{left:511px;top:4px}
.status .battery{left:580px;top:9px;width:44px;height:19px;border:2px solid var(--white);border-radius:4px;padding:2px}
.status .battery i{display:block;height:100%;background:var(--white);border-radius:1px}

/* title */
.title{left:20px;top:46px;color:var(--brown);font-size:50px;font-weight:400;letter-spacing:-1px}
.title small{color:var(--white);font-size:36px;letter-spacing:0}

/* selectors */
.select{top:113px;width:290px;height:46px;background:var(--cream);display:flex;align-items:center;padding-left:10px;color:var(--accent);font-size:20px;font-weight:300}
.select svg{margin-left:12px}
.select .caret{position:absolute;right:12px;top:16px;width:0;height:0;border-left:9px solid transparent;border-right:9px solid transparent;border-top:14px solid var(--brown-dark)}

/* level cards */
.level-card{top:178px;width:137px;height:137px;background:var(--card);border:2px solid var(--card-edge);border-radius:14px;box-shadow:0 3px 0 var(--card-edge);text-align:center;color:var(--white)}
.level-card .avatar{margin:8px auto 0;width:76px;height:76px;border-radius:50%;background:radial-gradient(circle at 50% 40%,#f6d2b4 0 30%,#a0522d 31% 55%,var(--white) 56%)}
.level-card p{font-family:"Roboto Condensed",sans-serif;font-size:12px;line-height:13px;margin-top:2px;padding:0 4px}
.level-card h3{font-size:17px;color:#4a1e04;font-weight:700;margin-top:2px}

.progress{left:19px;top:328px;width:596px;height:11px;background:#f4a36a}
.progress i{display:block;width:506px;height:100%;background:var(--brown)}
.progress b{position:absolute;right:0;top:0;width:8px;height:100%;background:var(--brown)}

/* menu */
.menu-item{top:366px;width:112px;height:112px;border-radius:50%;background:var(--circle);box-shadow:0 0 0 5px rgba(255,190,140,.45);color:var(--white);text-align:center;font-size:11px}
.menu-item::before{content:"";position:absolute;inset:7px;border-radius:50%;border:2px dotted rgba(255,255,255,.75)}
.menu-item.active{background:var(--brown-dark);box-shadow:0 0 0 6px #f2a36f}
.menu-item svg{position:absolute;left:31px;top:18px}
.menu-item span{position:absolute;left:0;right:0;top:74px}

/* messages */
.bubble{width:514px;height:120px;background:var(--bubble)}
.bubble .fold{position:absolute;top:0;width:34px;height:34px}
.hex-wrap{position:absolute;width:94px;height:96px;clip-path:polygon(25% 2%,75% 2%,100% 50%,75% 98%,25% 98%,0 50%);background:var(--hex-line)}
.hex-wrap .photo{position:absolute;inset:2px;clip-path:inherit}
.time{position:absolute;height:24px;padding:0 9px;border-radius:12px;background:var(--pill);color:var(--white);font-size:12px;line-height:24px}
.msg{position:absolute;color:var(--msg-text);font-size:18px;line-height:26px}
.lvl-badge{position:absolute;text-align:center;color:var(--white);font-weight:700;font-size:16px}
.lvl-badge .avatar{width:84px;height:84px;border-radius:50%;margin:0 auto 2px}

/* profile */
.profile{left:0;top:948px;width:640px;height:188px;background:var(--cream)}
.profile h2{position:absolute;left:0;right:0;top:8px;text-align:center;color:var(--accent);font-size:24px;font-weight:300}
.profile .rule{position:absolute;top:22px;height:1px;background:#e0b58a}
.friend{position:absolute;top:44px;width:118px;text-align:center}
.friend .hex-wrap{position:relative;margin:0 auto;width:96px;height:96px;background:var(--profile-line)}
.friend h4{color:#d2461a;font-size:16px;font-weight:400;margin-top:4px}
.friend small{display:block;color:#d2461a;font-size:10px}
.friend small svg{vertical-align:-1px;margin-right:3px}
</style>
</head>
<body>
<div class="screen">

  <div class="abs status">
    <div class="abs dots"><span></span><span></span><span></span><span></span><span class="off"></span></div>
    <div class="abs carrier">Carrier
      <svg width="24" height="18" viewBox="0 0 24 18" style="margin-left:10px;vertical-align:-1px"><path d="M12 16l3-3a4 4 0 0 0-6 0zM6 10a8.5 8.5 0 0 1 12 0l2-2a11.5 11.5 0 0 0-16 0zM1 5a15.5 15.5 0 0 1 22 0l1-1.6A17.5 17.5 0 0 0 0 3.4z" fill="#fff"/></svg>
    </div>
    <svg class="abs" style="left:477px;top:8px" width="20" height="20" viewBox="0 0 20 20"><circle cx="10" cy="10" r="8" fill="none" stroke="#fff" stroke-width="2"/><rect x="7" y="9" width="6" height="5" fill="#fff"/><path d="M8 9V7a2 2 0 0 1 4 0v2" fill="none" stroke="#fff" stroke-width="1.5"/></svg>
    <div class="abs pct">100%</div>
    <div class="abs battery"><i></i></div>
  </div>

  <h1 class="abs title">Lets <small>PLAY GAME...</small></h1>

  <div class="abs select" style="left:18px">Select Level
    <svg width="26" height="26" viewBox="0 0 26 26"><polygon points="13,1 16,6 22,4 21,10 25,13 21,16 22,22 16,20 13,25 10,20 4,22 5,16 1,13 5,10 4,4 10,6" fill="var(--accent)"/></svg>
    <i class="caret"></i>
  </div>
  <div class="abs select" style="left:327px">Select Player
    <svg width="28" height="28" viewBox="0 0 28 28"><circle cx="14" cy="14" r="13" fill="var(--accent)"/><circle cx="14" cy="11" r="5" fill="none" stroke="var(--cream)" stroke-width="2"/><path d="M6 23c2-5 14-5 16 0" fill="none" stroke="var(--cream)" stroke-width="2"/></svg>
    <i class="caret"></i>
  </div>

  <div class="abs level-card" style="left:17px"><div class="avatar" role="img" aria-label="Cartoon level character avatar"></div><p>Lorem ipsum dolor sit amet, consectetuer...</p><h3>LEVEL 1</h3></div>
  <div class="abs level-card" style="left:172px"><div class="avatar" role="img" aria-label="Cartoon level character avatar"></div><p>Lorem ipsum dolor sit amet, consectetuer...</p><h3>LEVEL 2</h3></div>
  <div class="abs level-card" style="left:328px"><div class="avatar" role="img" aria-label="Cartoon level character avatar"></div><p>Lorem ipsum dolor sit amet, consectetuer...</p><h3>LEVEL 3</h3></div>
  <div class="abs level-card" style="left:483px"><div class="avatar" role="img" aria-label="Cartoon level character avatar"></div><p>Lorem ipsum dolor sit amet, consectetuer...</p><h3>LEVEL 4</h3></div>

  <div class="abs progress"><i></i><b></b></div>

  <nav>
    <div class="abs menu-item active" style="left:10px">
      <svg width="50" height="50" viewBox="0 0 50 50" fill="none" stroke="var(--gold)" stroke-width="2.5"><circle cx="25" cy="25" r="8"/><path d="M21 3h8l1 6 5 2 5-4 6 6-4 5 2 5 6 1v8l-6 1-2 5 4 5-6 6-5-4-5 2-1 6h-8l-1-6-5-2-5 4-6-6 4-5-2-5-6-1v-8l6-1 2-5-4-5 6-6 5 4 5-2z"/></svg>
      <span>Settings</span>
    </div>
    <div class="abs menu-item" style="left:133px">
      <svg width="52" height="50" viewBox="0 0 52 50" fill="none" stroke="var(--gold)" stroke-width="2.5"><path d="M2 6h8l7 24h26l6-18H14"/><path d="M18 22h28"/><circle cx="20" cy="40" r="4"/><circle cx="40" cy="40" r="4"/></svg>
      <span>Shop</span>
    </div>
    <div class="abs menu-item" style="left:260px">
      <svg width="50" height="50" viewBox="0 0 50 50" fill="var(--gold)"><path d="M4 14l11 10 10-16 10 16 11-10-4 22H8z"/><rect x="8" y="38" width="34" height="5"/><circle cx="4" cy="12" r="3"/><circle cx="25" cy="6" r="3"/><circle cx="46" cy="12" r="3"/></svg>
      <span>Leaderboards</span>
    </div>
    <div class="abs menu-item" style="left:383px">
      <svg width="50" height="50" viewBox="0 0 50 50" fill="none" stroke="var(--gold)" stroke-width="2.5"><circle cx="25" cy="17" r="13"/><circle cx="25" cy="17" r="7"/><path d="M17 28l-4 17 6-4 4 6 2-16M33 28l4 17-6-4-4 6"/></svg>
      <span>Achievements</span>
    </div>
    <div class="abs menu-item" style="left:510px">
      <svg width="50" height="50" viewBox="0 0 50 50"><text x="25" y="44" text-anchor="middle" font-family="Roboto,sans-serif" font-size="50" fill="var(--gold)">?</text></svg>
      <span>Help</span>
    </div>
  </nav>

  <section>
    <div class="abs bubble" style="left:27px;top:511px">
      <svg class="fold" style="right:0" viewBox="0 0 34 34"><polygon points="0,0 34,34 0,34" fill="var(--bubble-fold)"/><polygon points="0,0 34,0 34,34" fill="#f7891e"/></svg>
      <div class="hex-wrap" style="left:16px;top:12px"><div class="photo" role="img" aria-label="Profile photo of Megan" style="background:linear-gradient(160deg,#6b4a3a,#d9a88c)"></div></div>
      <span class="time" style="left:131px;top:13px">Today 5:55 PM</span>
      <p class="msg" style="left:129px;top:46px">Hey What's Up. What are you doing..<br>Do you wanna be play something...</p>
    </div>

    <div class="abs bubble" style="left:107px;top:658px;width:504px">
      <svg class="fold" style="left:0" viewBox="0 0 34 34"><polygon points="34,0 0,34 34,34" fill="var(--bubble-fold)"/><polygon points="0,0 34,0 0,34" fill="#f7891e"/></svg>
      <div class="hex-wrap" style="left:36px;top:12px"><div class="photo" role="img" aria-label="Profile photo of Emma" style="background:linear-gradient(160deg,#e8c88a,#d99a78)"></div></div>
      <span class="time" style="left:152px;top:27px">Today 5:58 PM</span>
      <p class="msg" style="left:154px;top:57px">Hey Lets Play Level 2...</p>
      <div class="lvl-badge" style="left:401px;top:9px"><div class="avatar" role="img" aria-label="Level 2 character avatar" style="background:radial-gradient(circle at 50% 42%,#f6d2b4 0 28%,#a0522d 29% 52%,#fff 53%)"></div>LEVEL 2</div>
    </div>

    <div class="abs bubble" style="left:27px;top:805px">
      <svg class="fold" style="right:0" viewBox="0 0 34 34"><polygon points="0,0 34,34 0,34" fill="var(--bubble-fold)"/><polygon points="0,0 34,0 34,34" fill="#f7891e"/></svg>
      <div class="hex-wrap" style="left:16px;top:16px"><div class="photo" role="img" aria-label="Profile photo of Megan" style="background:linear-gradient(160deg,#6b4a3a,#d9a88c)"></div></div>
      <span class="time" style="left:131px;top:15px">Today 6:05 PM</span>
      <p class="msg" style="left:132px;top:45px">I Just played level 2.<br>Why don't you play this too?</p>
      <div class="lvl-badge" style="left:386px;top:14px"><div class="avatar" role="img" aria-label="Level 3 character avatar" style="background:radial-gradient(circle at 50% 42%,#f6d2b4 0 28%,#2a1a14 29% 52%,#fff 53%)"></div>LEVEL 3</div>
    </div>
  </section>

  <section class="abs profile">
    <span class="rule" style="left:28px;width:230px"></span>
    <h2>PROFILE</h2>
    <span class="rule" style="left:382px;width:222px"></span>

    <div class="friend" style="left:25px"><div class="hex-wrap"><div class="photo" role="img" aria-label="Profile photo of Megan" style="background:linear-gradient(160deg,#6b4a3a,#d9a88c)"></div></div><h4>Megan</h4><small><svg width="8" height="10" viewBox="0 0 8 10"><path d="M4 10L1 5a3 3 0 1 1 6 0z" fill="#999"/></svg>Los Angeles, USA</small></div>
    <div class="friend" style="left:142px"><div class="hex-wrap"><div class="photo" role="img" aria-label="Profile photo of Emma" style="background:linear-gradient(160deg,#e8c88a,#d99a78)"></div></div><h4>Emma</h4><small><svg width="8" height="10" viewBox="0 0 8 10"><path d="M4 10L1 5a3 3 0 1 1 6 0z" fill="#999"/></svg>Paris, France</small></div>
    <div class="friend" style="left:260px"><div class="hex-wrap"><div class="photo" role="img" aria-label="Profile photo of Amanda" style="background:linear-gradient(160deg,#4a3428,#c99a80)"></div></div><h4>Amanda</h4><small><svg width="8" height="10" viewBox="0 0 8 10"><path d="M4 10L1 5a3 3 0 1 1 6 0z" fill="#999"/></svg>Florence Itly</small></div>
    <div class="friend" style="left:378px"><div class="hex-wrap"><div class="photo" role="img" aria-label="Profile photo of Linda" style="background:linear-gradient(160deg,#222,#8a8a8a)"></div></div><h4>Linda</h4><small><svg width="8" height="10" viewBox="0 0 8 10"><path d="M4 10L1 5a3 3 0 1 1 6 0z" fill="#999"/></svg>Cape Town, South Africa</small></div>
    <div class="friend" style="left:496px"><div class="hex-wrap"><div class="photo" role="img" aria-label="Profile photo of Adriana" style="background:linear-gradient(160deg,#333,#b0b0b0)"></div></div><h4>Adriana</h4><small><svg width="8" height="10" viewBox="0 0 8 10"><path d="M4 10L1 5a3 3 0 1 1 6 0z" fill="#999"/></svg>Los Angeles, USA</small></div>
  </section>

</div>
</body>
</html>
```